Visitenkarte für Selbständigen
Zielgruppe
Ich bin Selbständiger Unternehmer, der sowohl Versicherungs/Finanzprodukte vertreibt, sowie Immobilien zur Kapitalanlage.
Aufgabenstellung
Ich hätte gern eine zweiseitige Karte. Vorderseite Name und meine Initialen als Logo.
Rückseite Name, Anschrift und telnr.
Berufsbezeichnung muss nicht zwingend mit auf der Karte sein.
Die Karte sollte schwarz oder weiß sein und auf der Vorderseite Name und Logo in Silber (Spiegel Folie)
Lars Hofmeier
Lindenweg 17
74821 Mosbachtal
email: info@lars-hofmeier.de
Tel 0151-38472916
Fax 06399-7281904

```html
<!DOCTYPE html>
<html lang="de">
<head>
<meta charset="utf-8">
<title>Visitenkarte Lars Hofmeier</title>
<link href="https://fonts.googleapis.com/css2?family=PT+Serif:wght@400;700&display=swap" rel="stylesheet">
<style>
  :root {
    --stage: #68766c;
    --paper-light: #ffffff;
    --paper-dark: #000000;
    --band: #9a9a9a;
    --ink-light: #8c8c8c;
    --ink-dark: #a9a9a9;
    --silver: #a0a0a0;
    --shadow: rgba(30, 40, 34, 0.45);
  }
  * { margin: 0; padding: 0; box-sizing: border-box; }
  html, body { width: 1200px; height: 708px; overflow: hidden; }
  body {
    background: var(--stage);
    position: relative;
    font-family: "PT Serif", Georgia, serif;
  }
  .card {
    position: absolute;
    top: 176px;
    width: 225px;
    height: 348px;
    box-shadow: 6px 7px 9px var(--shadow);
    text-align: center;
    overflow: hidden;
  }
  .card--light { background: var(--paper-light); color: var(--ink-light); }
  .card--dark { background: var(--paper-dark); color: var(--ink-dark); }
  .card--1 { left: 63px; }
  .card--2 { left: 314px; }
  .card--3 { left: 647px; }
  .card--4 { left: 897px; }

  .band {
    position: absolute;
    left: 0; right: 0;
    top: 231px;
    height: 10px;
    background: var(--band);
  }
  .name {
    position: absolute;
    left: 0; right: 0;
    font-size: 15px;
    font-variant: small-caps;
    letter-spacing: 2px;
    line-height: 1;
  }
  .name--top { top: 69px; }
  .name--bottom { top: 287px; }
  .contact {
    position: absolute;
    left: 0; right: 0;
    font-weight: 700;
    font-size: 10.5px;
    letter-spacing: 0.9px;
    line-height: 14.5px;
  }
  .contact--address { top: 104px; }
  .contact--reach { top: 141px; line-height: 15px; }

  .mark {
    position: absolute;
    left: 0; right: 0;
  }
  .mark--large { top: 52px; }
  .mark--small { top: 260px; }
  .mark svg { display: block; margin: 0 auto; }
  .mark-name {
    display: block;
    font-size: 12px;
    font-variant: small-caps;
    letter-spacing: 1.5px;
    line-height: 1;
    color: var(--silver);
    margin-top: 8px;
  }
  .mark--small .mark-name { font-size: 10px; margin-top: 5px; }
</style>
</head>
<body>

  <section class="card card--light card--1">
    <p class="name name--top">Lars Hofmeier</p>
    <p class="contact contact--address">Lindenweg 17<br>74821 Mosbachtal</p>
    <p class="contact contact--reach">Email: info@lars-hofmeier.de<br>Tel: 0151-38472916<br>Fax: 06399-7281904</p>
    <div class="band"></div>
    <div class="mark mark--small">
      <svg width="46" height="46" viewBox="0 0 46 46"><circle cx="23" cy="23" r="21" fill="none" stroke="var(--silver)" stroke-width="3"/></svg>
      <span class="mark-name">Lars Hofmeier</span>
    </div>
  </section>

  <section class="card card--light card--2">
    <div class="mark mark--large">
      <svg width="120" height="120" viewBox="0 0 120 120"><circle cx="60" cy="60" r="56" fill="none" stroke="var(--silver)" stroke-width="5"/></svg>
      <span class="mark-name">Lars Hofmeier</span>
    </div>
    <div class="band"></div>
    <p class="name name--bottom">Lars Hofmeier</p>
  </section>

  <section class="card card--dark card--3">
    <p class="name name--top">Lars Hofmeier</p>
    <p class="contact contact--address">Lindenweg 17<br>74821 Mosbachtal</p>
    <p class="contact contact--reach">Email: info@lars-hofmeier.de<br>Tel: 0151-38472916<br>Fax: 06399-7281904</p>
    <div class="band"></div>
    <div class="mark mark--small">
      <svg width="46" height="46" viewBox="0 0 46 46"><circle cx="23" cy="23" r="21" fill="none" stroke="var(--silver)" stroke-width="3"/></svg>
      <span class="mark-name">Lars Hofmeier</span>
    </div>
  </section>

  <section class="card card--dark card--4">
    <div class="mark mark--large">
      <svg width="120" height="120" viewBox="0 0 120 120"><circle cx="60" cy="60" r="56" fill="none" stroke="var(--silver)" stroke-width="5"/></svg>
      <span class="mark-name">Lars Hofmeier</span>
    </div>
    <div class="band"></div>
    <p class="name name--bottom">Lars Hofmeier</p>
  </section>

</body>
</html>
```